Consulting im Pharmaproduktionsbereich sucht Webdesign
Zielgruppe
Consulting im Pharmaproduktionsbereich.
Bitte lesen Sie dazu die PowerPoint.
Aufgabenstellung
Im Anhang finden Sie eine Powerpoint Datei, von welcher die 'Home' und 'Referenz'seite Teil dieser Auschreibung sind.

```html
<!DOCTYPE html>
<html lang="de">
<head>
<meta charset="utf-8">
<title>Norvalt Pharma – Pharma Know-how</title>
<link rel="stylesheet" href="https://fonts.googleapis.com/css2?family=Tinos:wght@700&family=Open+Sans:ital,wght@0,400;1,400&family=Raleway:wght@400;600&family=Fira+Sans:ital,wght@0,300;0,400;1,300;1,400&display=swap">
<style>
:root{
  --navy:#1b4a8c;
  --footer:#17478a;
  --slate:#5d737c;
  --slate-text:#5b6d78;
  --band:#f1f2f4;
  --field:#f0f1f3;
  --ink:#1d2730;
  --white:#ffffff;
}
*{margin:0;padding:0;box-sizing:border-box}
html,body{width:884px;height:1200px;overflow:hidden;background:var(--white)}
.page{position:relative;width:884px;height:1200px;font-family:"Open Sans",sans-serif;color:var(--ink)}
.abs{position:absolute}

/* hero */
.hero{left:0;top:0;width:884px;height:416px;background:linear-gradient(100deg,#f3f5f9 0%,#e4eaf2 35%,#c9d6e6 65%,#a9bdd8 100%)}
.brand{left:80px;top:15px;font-family:"Raleway",sans-serif;font-weight:600;font-size:24px;color:var(--navy);display:flex;align-items:center;gap:8px}
.brand .mark{width:22px;height:22px;background:var(--navy);border-radius:4px}
.nav{right:61px;top:19px;font-family:"Raleway",sans-serif;font-size:10px;color:var(--navy);display:flex;align-items:center;gap:6px}
.nav .active{font-weight:600;color:#111}
.nav .call{width:20px;height:20px;border-radius:50%;background:var(--navy);display:flex;align-items:center;justify-content:center;margin-left:4px}
.hero-title{right:84px;top:102px;text-align:right;font-family:"Tinos",serif;font-weight:700;font-size:41px;line-height:45px;color:var(--navy)}
.hero-sub{right:84px;top:188px;font-family:"Fira Sans",sans-serif;font-style:italic;font-weight:300;font-size:23px;color:var(--slate-text)}
.hero-btn{left:633px;top:225px;width:167px;height:26px;background:var(--slate);color:var(--white);font-family:"Fira Sans",sans-serif;font-weight:400;font-size:11.5px;letter-spacing:.4px;display:flex;align-items:center;justify-content:center}
.intro-tab{left:131px;top:388px;width:646px;height:28px;background:var(--white)}

/* intro */
.intro{left:131px;top:409px;width:646px;text-align:center}
.intro h1{font-family:"Tinos",serif;font-weight:700;font-size:27px;color:var(--navy);line-height:34px}
.intro h2{font-family:"Open Sans",sans-serif;font-style:italic;font-weight:400;font-size:15px;color:var(--slate-text)}
.intro p{font-style:italic;font-size:9.6px;line-height:12px;margin:10px auto 0;width:540px}

/* cards */
.band{left:0;top:613px;width:884px;height:142px;background:var(--band)}
.card{top:523px;width:238px;height:182px;overflow:hidden}
.card .photo{position:absolute;left:0;top:0;width:100%;height:145px}
.card .label{position:absolute;left:0;bottom:0;width:100%;height:37px;background:var(--slate);color:var(--white);font-family:"Tinos",serif;font-weight:700;font-size:25px;display:flex;align-items:center;justify-content:center}
.card-value{left:588px;top:522px;width:238px;height:182px;background:#5f7680;color:var(--white);text-align:center;padding:22px 18px 0}
.card-value h3{font-family:"Tinos",serif;font-weight:700;font-size:26px;line-height:26px}
.card-value p{font-style:italic;font-size:11.3px;line-height:15px;margin-top:2px}

/* contact */
.portrait{left:71px;top:803px;width:180px;height:180px;border-radius:50%;background:radial-gradient(circle at 50% 45%,#f5f6f8 0%,#e1e5ea 60%,#c9d0d8 100%)}
.pitch{left:289px;top:803px;width:230px;font-family:"Fira Sans",sans-serif;font-weight:400}
.pitch .kicker{font-size:11.5px;color:var(--navy);letter-spacing:.3px}
.pitch .lead{font-size:11.5px;color:var(--slate-text);font-weight:300;margin-top:1px}
.pitch .body{font-size:11.5px;line-height:14.5px;margin-top:12px;color:#111}
.address{left:290px;top:909px;font-family:"Fira Sans",sans-serif;font-weight:400;font-size:8.6px;color:#111}
.address .row{display:flex;align-items:flex-start;gap:5px;margin-bottom:10px}
.address svg{flex:none}
.form-title{left:580px;top:796px;font-family:"Tinos",serif;font-weight:700;font-size:27px;color:var(--navy)}
.form{left:581px;top:834px;width:238px;font-family:"Fira Sans",sans-serif;font-weight:400;font-size:7.4px;color:#111}
.form .lbl{display:flex;align-items:center;gap:3px;height:10px}
.form .field{height:22px;background:var(--field);margin:4px 0 9px}
.form .select{height:22px;background:var(--field);margin-top:4px;display:flex;align-items:center;justify-content:space-between;padding:0 5px;font-style:italic}
.form-note{left:581px;top:970px;font-family:"Fira Sans",sans-serif;font-weight:400;font-size:5px;line-height:8px;color:#333}
.form-btn{left:748px;top:966px;width:70px;height:20px;background:var(--slate);color:var(--white);font-family:"Fira Sans",sans-serif;font-weight:400;font-size:9.5px;display:flex;align-items:center;justify-content:center}

/* footer */
.footer{left:0;top:1059px;width:884px;height:141px;background:var(--footer)}
.footer-brand{left:0;top:1088px;width:884px;display:flex;justify-content:center;align-items:center;gap:9px;font-family:"Raleway",sans-serif;font-weight:600;font-size:28px;color:#143a70}
.footer-brand .mark{width:26px;height:26px;background:#143a70;border-radius:4px}
.footer-rule{left:68px;top:1139px;width:748px;height:1px;background:#5f82b5}
.footer-nav{left:68px;top:1149px;font-family:"Raleway",sans-serif;font-size:10px;color:var(--white);display:flex;gap:7px}
.footer-nav b{font-weight:600}
.copy{left:68px;top:1163px;font-family:"Raleway",sans-serif;font-size:9.6px;color:var(--white)}
.social{left:802px;top:1148px;width:14px;height:14px;background:var(--white);border-radius:1px}
</style>
</head>
<body>
<div class="page">
  <div class="abs hero" role="img" aria-label="Foto: Laborantin mit Schutzbrille und Pipette über einer Petrischale mit Keimling"></div>
  <div class="abs brand"><span class="mark"></span>Norvalt Pharma</div>
  <nav class="abs nav">
    <span class="active">HOME</span><span>|</span><span>REFERENZEN</span><span>|</span><span>KONTAKT</span><span>|</span><span>IMPRESSUM</span>
    <span class="call"><svg width="11" height="11" viewBox="0 0 24 24"><path fill="#fff" d="M6.6 10.8c1.4 2.8 3.8 5.1 6.6 6.6l2.2-2.2c.3-.3.7-.4 1-.2 1.1.4 2.3.6 3.6.6.6 0 1 .4 1 1V20c0 .6-.4 1-1 1C10.6 21 3 13.4 3 4c0-.6.4-1 1-1h3.5c.6 0 1 .4 1 1 0 1.3.2 2.5.6 3.6.1.3 0 .7-.2 1z"/></svg></span>
  </nav>
  <div class="abs hero-title">PHARMA<br>KNOW-HOW</div>
  <div class="abs hero-sub">für Ihr Unternehmen</div>
  <div class="abs hero-btn">JETZT KONTAKT AUFNEHMEN</div>
  <div class="abs intro-tab"></div>

  <section class="abs intro">
    <h1>Als spezialisierter Anbieter</h1>
    <h2>schaffen wir Wert in der Pharma-Produktion</h2>
    <p>Mit langjähriger Erfahrung in Abläufen und überlegener Technologie setzt ein Netzwerk von Spitzenleuten schnell und pragmatisch um Sicht- und messbar in Ihrer Bilanz</p>
  </section>

  <div class="abs band"></div>
  <div class="abs card" style="left:78px">
    <div class="photo" role="img" aria-label="Foto: Berater und Ärztin im Gespräch am Schreibtisch" style="background:linear-gradient(120deg,#d9dde2,#eef0f2 55%,#c8cdd4)"></div>
    <div class="label">Abläufe</div>
  </div>
  <div class="abs card" style="left:331px">
    <div class="photo" role="img" aria-label="Foto: Reinraumlabor mit Bildschirmen und Mikroskop" style="background:linear-gradient(160deg,#e6ecf3,#b9c6d4 60%,#dfe5ec)"></div>
    <div class="label">Technologie</div>
  </div>
  <div class="abs card-value" role="img" aria-label="Hintergrund: abgedunkeltes Foto einer Besprechung">
    <h3>Wert</h3>
    <p>Ob Sie Topline mehr Kapazität generieren wollen, oder Bottomline einzelne Kostenpositionen reduzieren: Wir achten auf das für Ihren Betrieb passende Werteversprechen und liefern schnell ergebniswirksam. Unnötiger Firlefanz bleibt weg.</p>
  </div>

  <div class="abs portrait" role="img" aria-label="Foto: Hand mit Füllfederhalter beim Schreiben"></div>
  <div class="abs pitch">
    <div class="kicker">HABEN WIR IHR INTERESSE GEWECKT?</div>
    <div class="lead">Treten Sie mit uns in Kontakt</div>
    <div class="body">Vereinbaren SIe doch gleich mit uns ein kostenloses Erstgespräch. Wir lassen Ihr Unternehmen wachsen.</div>
  </div>
  <div class="abs address">
    <div class="row"><svg width="10" height="13" viewBox="0 0 10 13"><path fill="#1b4a8c" d="M5 0a5 5 0 0 1 5 5c0 3.5-5 8-5 8S0 8.5 0 5a5 5 0 0 1 5-5zm0 3a2 2 0 1 0 0 4 2 2 0 0 0 0-4z"/></svg><span>Norvalt Pharma<br>Lindenweg 12, 79100 Feldhausen</span></div>
    <div class="row"><svg width="9" height="13" viewBox="0 0 9 13"><rect x="1" y="0.8" width="7" height="11.4" rx="1.2" fill="none" stroke="#1b4a8c" stroke-width="1.4"/><rect x="3.5" y="10" width="2" height="1" fill="#1b4a8c"/></svg><span>Tel. (0) 5550 / 210 210</span></div>
    <div class="row"><svg width="11" height="11" viewBox="0 0 11 11"><circle cx="5.5" cy="5.5" r="4.8" fill="none" stroke="#1b4a8c" stroke-width="1.3"/><path d="M.7 5.5h9.6M5.5.7v9.6" stroke="#1b4a8c" stroke-width="1"/></svg><span>info@norvalt-pharma.de</span></div>
  </div>

  <div class="abs form-title">KONTAKT</div>
  <form class="abs form">
    <div class="lbl"><svg width="7" height="7" viewBox="0 0 8 8"><circle cx="4" cy="2.2" r="2" fill="#111"/><path d="M0 8c0-2.5 1.8-3.5 4-3.5S8 5.5 8 8z" fill="#111"/></svg>Ihr Name*</div>
    <div class="field"></div>
    <div class="lbl"><svg width="8" height="7" viewBox="0 0 8 7"><path d="M0 2.5C1 .8 7 .8 8 2.5L7 3.5 5.5 2.8V2h-3v.8L1 3.5zM1.5 4h5l.5 3H1z" fill="#111"/></svg>Telefonnummer*</div>
    <div class="field"></div>
    <div class="lbl"><svg width="7" height="7" viewBox="0 0 8 8"><circle cx="4" cy="2.2" r="2" fill="#111"/><path d="M0 8c0-2.5 1.8-3.5 4-3.5S8 5.5 8 8z" fill="#111"/></svg>Ich habe Interesse an</div>
    <div class="select"><span>einem kostenfreien Erstgespräch</span><svg width="11" height="7" viewBox="0 0 11 7"><path d="M1 1l4.5 4.5L10 1" fill="none" stroke="#111" stroke-width="2"/></svg></div>
  </form>
  <div class="abs form-note">Die mit * gekennzeichneten Felder sind Pflichtfelder.<br>Ihre Daten werden vertraulich behandelt.</div>
  <div class="abs form-btn">AB DIE POST</div>

  <footer class="abs footer"></footer>
  <div class="abs footer-brand"><span class="mark"></span>Norvalt Pharma</div>
  <div class="abs footer-rule"></div>
  <div class="abs footer-nav"><b>HOME</b><span>|</span><span>REFERENZEN</span><span>|</span><span>KONTAKT</span><span>|</span><span>IMPRESSUM</span><span>|</span><span>DATENSCHUTZ</span></div>
  <div class="abs copy">© Norvalt Pharma 2019. All rights reserved.</div>
  <div class="abs social"></div>
</div>
</body>
</html>
```